Contemporary Media Company with Logo Needs Business Card Design

Need a modern card design for a full service digital media company using the logo included. Also want the info below on the card. Probably list the services on the card back to save space for the front. Want something contemporary to impress prospective clients. You may want to submit both a somewhat more conservative design, and then a more wild one.
General Info: (this phrase need not be on the card)
Tod Parvin
Founder and CEO
949-628-4513
tod@lumavantstudio.example
lumavantstudio.example
Services: (this word need not be on the card)
Content & Experience Strategy
Brand Development
Search Engine Optimization
Website Design
Website Operation
Social Media Integration
Complete Video Solutions
Industry/Entity Type
Business
Contact Information for Business Card
Tod Parvin
Founder and CEO
949-628-4513
tod@lumavantstudio.example
lumavantstudio.example
Brand Development
Website Design
Website Operation
Social Media Integration
Complete Video Solutions
Look and feel

```html
<!DOCTYPE html>
<html lang="en">
<head>
<meta charset="utf-8">
<title>Lumavant Studio — Business Card</title>
<link href="https://fonts.googleapis.com/css2?family=Open+Sans:wght@400;600;700&display=swap" rel="stylesheet">
<style>
  :root {
    --page-bg: #ece9e5;
    --navy: #1f2c3a;
    --navy-light: #2a3a4b;
    --orange: #f08a1d;
    --logo-grey: #c9ccd0;
    --white: #ffffff;
    --ink: #1c1c1c;
    --ink-soft: #333333;
  }
  * { box-sizing: border-box; margin: 0; padding: 0; }
  html, body {
    width: 1200px; height: 1200px; overflow: hidden;
    background: var(--page-bg);
    font-family: "Open Sans", Arial, sans-serif;
  }
  .card {
    position: absolute; left: 240px; width: 720px; height: 405px;
    overflow: hidden;
    box-shadow: 0 6px 16px rgba(0,0,0,0.18);
  }
  .card-front { top: 110px; }
  .card-back { top: 650px; background: var(--white); }

  .card-surface {
    position: absolute; inset: 0;
    background: linear-gradient(160deg, var(--navy-light) 0%, var(--navy) 70%);
  }
  .card-back .card-surface { top: 162px; }

  .brand-lockup {
    position: absolute; top: 50%; left: 50%;
    transform: translate(-50%, -50%);
    display: flex; align-items: center; gap: 22px;
  }
  .brand-square { width: 56px; height: 56px; background: var(--orange); }
  .brand-name {
    color: var(--logo-grey); font-weight: 600;
    font-size: 40px; letter-spacing: 3px; text-transform: uppercase;
    white-space: nowrap;
  }

  .identity {
    position: absolute; top: 52px; left: 408px;
    display: flex; align-items: center; gap: 34px;
  }
  .identity-square { width: 62px; height: 62px; background: var(--orange); }
  .person-name { font-size: 23px; font-weight: 700; color: var(--ink); line-height: 1.2; }
  .person-title { font-size: 16px; color: var(--ink-soft); line-height: 1.3; }

  .contact-list {
    position: absolute; left: 58px; top: 236px; list-style: none;
  }
  .contact-item {
    display: flex; align-items: center; gap: 16px;
    color: var(--white); font-size: 16.5px; height: 34px;
  }
  .contact-icon { width: 20px; height: 20px; flex: none; }

  .service-list {
    position: absolute; left: 442px; top: 200px; list-style: none;
  }
  .service-item {
    color: var(--white); font-size: 14px; height: 24px; line-height: 24px;
    position: relative; padding-left: 22px;
  }
  .service-item::before {
    content: ""; position: absolute; left: 2px; top: 9px;
    width: 6px; height: 6px; border-radius: 50%; background: var(--white);
  }
</style>
</head>
<body>

<section class="card card-front">
  <div class="card-surface" role="img" aria-label="Dark navy background with a subtle triangle texture"></div>
  <div class="brand-lockup">
    <span class="brand-square"></span>
    <span class="brand-name">Lumavant Studio</span>
  </div>
</section>

<section class="card card-back">
  <div class="identity">
    <span class="identity-square"></span>
    <div>
      <p class="person-name">Tod Parvin</p>
      <p class="person-title">Founder and CEO</p>
    </div>
  </div>

  <div class="card-surface" role="img" aria-label="Dark navy background with a subtle triangle texture"></div>

  <ul class="contact-list">
    <li class="contact-item">
      <svg class="contact-icon" viewBox="0 0 24 24" fill="#fff" aria-hidden="true">
        <path d="M6.6 10.8a15.1 15.1 0 0 0 6.6 6.6l2.2-2.2a1 1 0 0 1 1-.25 11.4 11.4 0 0 0 3.6.57 1 1 0 0 1 1 1V20a1 1 0 0 1-1 1A17 17 0 0 1 3 4a1 1 0 0 1 1-1h3.5a1 1 0 0 1 1 1c0 1.25.2 2.45.57 3.57a1 1 0 0 1-.25 1z"/>
      </svg>
      <span>949-628-4513</span>
    </li>
    <li class="contact-item">
      <svg class="contact-icon" viewBox="0 0 24 24" fill="#fff" aria-hidden="true">
        <path d="M3 5h18a1 1 0 0 1 1 1v12a1 1 0 0 1-1 1H3a1 1 0 0 1-1-1V6a1 1 0 0 1 1-1zm1 2.2V17h16V7.2l-8 5.3z"/>
      </svg>
      <span>tod@lumavantstudio.example</span>
    </li>
    <li class="contact-item">
      <svg class="contact-icon" viewBox="0 0 24 24" fill="none" stroke="#fff" stroke-width="1.8" aria-hidden="true">
        <circle cx="12" cy="12" r="9"/>
        <ellipse cx="12" cy="12" rx="4" ry="9"/>
        <path d="M3 12h18M4.5 7.5h15M4.5 16.5h15"/>
      </svg>
      <span>lumavantstudio.example</span>
    </li>
  </ul>

  <ul class="service-list">
    <li class="service-item">Content &amp; Experience Strategy</li>
    <li class="service-item">Brand Development</li>
    <li class="service-item">Search Engine Optimization</li>
    <li class="service-item">Website Design</li>
    <li class="service-item">Website Operation</li>
    <li class="service-item">Social Media Integration</li>
    <li class="service-item">Complete Video Solutions</li>
  </ul>
</section>

</body>
</html>
```